Business card for STEADYWAVE

Please design professional business card for IT consulting firm STEADYWAVE INC.
Use logo attached.
Use information from sample qNode business card attached.
replace qnode inc with STEADYWAVE INC.
as well as qnodeinc.com with steadywave.example

```html
<!DOCTYPE html>
<html lang="en">
<head>
<meta charset="utf-8">
<title>STEADYWAVE – Business Card</title>
<link href="https://fonts.googleapis.com/css2?family=Lato:wght@300;700;900&family=Roboto+Condensed:wght@400;700&family=Montserrat:wght@400&display=swap" rel="stylesheet">
<style>
  :root {
    --backdrop: #2f2f2f;
    --card-light: #ffffff;
    --card-dark: #000000;
    --ink: #111111;
    --ink-soft: #4a4a4a;
    --brand-purple: #7b2d9b;
    --paper-white: #ffffff;
  }
  * { margin: 0; padding: 0; box-sizing: border-box; }
  html, body {
    width: 1200px; height: 1200px; overflow: hidden;
    background: var(--backdrop);
  }
  .card {
    position: absolute; left: 239px; width: 722px; height: 412px;
    border-radius: 26px;
  }
  .card--front { top: 140px; background: var(--card-light); }
  .card--back { top: 644px; background: var(--card-dark); }

  .wordmark {
    position: absolute; display: flex; align-items: center; gap: 14px;
    font-family: 'Lato', sans-serif; font-weight: 900;
    letter-spacing: 6px; line-height: 1;
  }
  .wordmark__square { width: 30px; height: 30px; background: var(--brand-purple); }
  .card--front .wordmark { left: 51px; top: 50px; font-size: 58px; color: var(--ink); }
  .card--back .wordmark {
    left: 0; right: 0; justify-content: center; top: 162px;
    font-size: 60px; color: var(--paper-white);
  }

  .holder { position: absolute; left: 51px; top: 166px; }
  .holder__name {
    font-family: 'Lato', sans-serif; font-weight: 700; font-size: 43px;
    color: var(--brand-purple); letter-spacing: -0.5px; line-height: 1;
  }
  .holder__credential { font-size: 21px; margin-left: 6px; letter-spacing: 0; }
  .holder__title {
    font-family: 'Lato', sans-serif; font-weight: 300; font-size: 23px;
    color: var(--ink-soft); letter-spacing: 1px; margin-top: 6px;
  }
  .divider {
    position: absolute; left: 51px; width: 623px; top: 255px;
    height: 3px; background: var(--ink);
  }

  .contact {
    position: absolute; top: 279px;
    font-family: 'Roboto Condensed', sans-serif; font-size: 20px;
    color: var(--ink); line-height: 30.5px;
  }
  .contact--personal { left: 51px; }
  .contact--company { left: 347px; }
  .contact__row { display: flex; align-items: center; gap: 8px; white-space: nowrap; }
  .contact__row--indent { padding-left: 22px; }
  .contact__icon { width: 14px; height: 14px; fill: var(--brand-purple); flex: none; }
  .contact__company {
    font-weight: 700; color: var(--brand-purple); font-size: 20px;
  }

  .site-url {
    position: absolute; left: 0; right: 0; top: 232px; text-align: center;
    font-family: 'Montserrat', sans-serif; font-size: 22px;
    color: var(--paper-white); letter-spacing: 1.5px;
  }
</style>
</head>
<body>
  <section class="card card--front">
    <div class="wordmark"><span>STEADYWAVE</span><span class="wordmark__square"></span></div>

    <div class="holder">
      <div class="holder__name">DORIAN VELASKO<span class="holder__credential">, P. ENG.</span></div>
      <div class="holder__title">GENERAL MANAGER</div>
    </div>

    <div class="divider"></div>

    <div class="contact contact--personal">
      <div class="contact__row">
        <svg class="contact__icon" viewBox="0 0 24 24"><path d="M6.6 10.8a15.1 15.1 0 0 0 6.6 6.6l2.2-2.2c.3-.3.7-.4 1-.2 1.1.4 2.3.6 3.6.6.6 0 1 .4 1 1V20c0 .6-.4 1-1 1A17 17 0 0 1 3 4c0-.6.4-1 1-1h3.5c.6 0 1 .4 1 1 0 1.3.2 2.5.6 3.6.1.3 0 .7-.2 1z"/></svg>
        <span>(905) 555 0140 ext.201</span>
      </div>
      <div class="contact__row">
        <svg class="contact__icon" viewBox="0 0 24 24"><path d="M6.6 10.8a15.1 15.1 0 0 0 6.6 6.6l2.2-2.2c.3-.3.7-.4 1-.2 1.1.4 2.3.6 3.6.6.6 0 1 .4 1 1V20c0 .6-.4 1-1 1A17 17 0 0 1 3 4c0-.6.4-1 1-1h3.5c.6 0 1 .4 1 1 0 1.3.2 2.5.6 3.6.1.3 0 .7-.2 1z"/></svg>
        <span>(416) 555 0187</span>
      </div>
      <div class="contact__row">
        <svg class="contact__icon" viewBox="0 0 24 24"><path d="M2 5h20v14H2z"/><path d="M3 6l9 6.3L21 6" fill="none" stroke="#fff" stroke-width="1.6"/></svg>
        <span>dvelasko@steadywave.example</span>
      </div>
    </div>

    <div class="contact contact--company">
      <div class="contact__row contact__company">STEADYWAVE INC.</div>
      <div class="contact__row">
        <svg class="contact__icon" viewBox="0 0 24 24"><path d="M12 2a7 7 0 0 0-7 7c0 5.2 7 13 7 13s7-7.8 7-13a7 7 0 0 0-7-7zm0 9.5A2.5 2.5 0 1 1 12 6.5a2.5 2.5 0 0 1 0 5z"/></svg>
        <span>1280 Harbourline Rd., Suite 101</span>
      </div>
      <div class="contact__row contact__row--indent">Mississauga, Ontario, L5A 0B9, Canada</div>
    </div>
  </section>

  <section class="card card--back">
    <div class="wordmark"><span>STEADYWAVE</span><span class="wordmark__square"></span></div>
    <div class="site-url">steadywave.example</div>
  </section>
</body>
</html>
```